Check, Perfect and Polish my Perfume Brochure

I will send my brochure to stores that sell perfumes.
The perfumes stores are located all around the world.

In this brochure/booklet I will tell the stores about my
1. my life
2. How I made perfumes on my own
3. I will talk about the perfumes I sell

I will use this brochure/booklet to make connections with perfume stores.
They should know, and remember who I am from this booklet.
I will use this brochure/booklet to make sales.

I need a graphic designer with
1. print experience
2. booklet and brochure making experience
3. very detailed eyes
4. good spelling
5. experience in fashion, health beauty products is important
6. please help me edit and polishing my brochure
7. my brochure to look very professional

This is the main point, to help me make my brochure look very cool, fashionable and professional

Target Market(s)

Perfume Store

Industry/Entity Type

perfumery, fashion, boutiques, high end luxury

Font styles to use
Serif

Colors
FFC000
F8CF3A
FAE287
FDF2CF
FEFAEE

Requirements
Must have
• 1. consistent design on all pages 2. have consistent colour and fonts 3. attractive photos 4. tell the stores about my brand 5. tell the stores about my life 6. tell the stores why my perfumes are very good
Nice to have
• I will like to have your personal style and suggestions please

```html
<!DOCTYPE html>
<html lang="en">
<head>
<meta charset="utf-8">
<title>Verell Perfumes – Brochure Pages</title>
<link href="https://fonts.googleapis.com/css2?family=Cinzel:wght@400;700&family=Playfair+Display:wght@400;800&family=Roboto:wght@400;500;700&display=swap" rel="stylesheet">
<style>
:root{
  --board:#f1f1f1;
  --paper:#ffffff;
  --brown:#5e3d31;
  --brown-deep:#4a2e25;
  --ink:#1b1b1b;
  --label:#3a3a3a;
  --gold:#f2a33a;
  --gold-deep:#d98a26;
  --cream:#fdf2cf;
  --frame:#e9e9e9;
}
*{margin:0;padding:0;box-sizing:border-box}
html,body{width:1200px;height:768px;overflow:hidden;background:var(--board)}
.board{position:relative;width:1200px;height:768px}
.page-label{position:absolute;font:400 16px/1 "Roboto",sans-serif;color:var(--label)}
.page{position:absolute;width:549px;height:309px;background:var(--paper);overflow:hidden;box-shadow:0 1px 3px rgba(0,0,0,.25)}
.page svg.band{position:absolute;left:0;top:0}
.title{position:absolute;left:0;width:100%;text-align:center;font-family:"Cinzel",serif;color:#fff;font-weight:400;white-space:nowrap}
.tagline{position:absolute;display:flex;align-items:center;justify-content:center;border:1.5px solid var(--gold);border-radius:12px;background:#7a4d2f;color:var(--cream);font-family:"Playfair Display",serif;white-space:nowrap}
.rule{position:absolute;height:1.5px;background:var(--gold)}
.rule::after{content:"";position:absolute;top:-3px;width:7px;height:7px;background:var(--gold);border-radius:50%}
.rule.left::after{left:0}
.rule.right::after{right:0}
.brand-seal{position:absolute;border-radius:50%;background:#fff;display:flex;align-items:center;justify-content:center}
.brand-seal span{display:flex;align-items:center;justify-content:center;width:86%;height:86%;border-radius:50%;border:2.5px solid var(--ink);font:700 17px/1 "Cinzel",serif;color:var(--ink);letter-spacing:1px}
.footer{position:absolute;top:289px;font:500 9px/1 "Roboto",sans-serif;color:var(--ink)}
.visual{position:absolute;left:0;top:0;width:100%;height:100%}
.portrait-frame{position:absolute;left:24px;top:110px;width:155px;height:157px;background:var(--frame);padding:5px}
.portrait{width:100%;height:100%;background:linear-gradient(160deg,#5b5e66 0%,#8b8680 45%,#c9b49a 70%,#7a4a3a 100%)}
.bio-name{position:absolute;left:201px;top:108px;font:800 18.5px/1 "Playfair Display",serif;color:var(--ink);letter-spacing:.2px}
.bio-role{position:absolute;left:201px;top:129px;font:500 8.6px/1 "Roboto",sans-serif;color:var(--ink)}
.timeline{position:absolute;left:201px;top:149px;list-style:none}
.timeline li{font:400 11px/19px "Roboto",sans-serif;color:var(--ink);display:flex;align-items:center;white-space:nowrap}
.timeline li::before{content:"";width:6px;height:6px;margin-right:6px;background:var(--ink);transform:rotate(45deg)}
.timeline b{font-weight:700;margin-right:3px}
</style>
</head>
<body>
<main class="board">

  <p class="page-label" style="left:32px;top:41px">Cover Page</p>
  <section class="page cover" style="left:30px;top:74px">
    <svg class="band" width="549" height="309" viewBox="0 0 549 309" aria-hidden="true">
      <path fill="var(--brown)" d="M0 148 a5.5 5 0 0 1 11 0 a5.5 5 0 0 1 11 0 a5.5 5 0 0 1 11 0 a5.5 5 0 0 1 11 0 a5.5 5 0 0 1 11 0 a5.5 5 0 0 1 11 0 a5.5 5 0 0 1 11 0 a5.5 5 0 0 1 11 0 a5.5 5 0 0 1 11 0 a5.5 5 0 0 1 11 0 a5.5 5 0 0 1 11 0 a5.5 5 0 0 1 11 0 a5.5 5 0 0 1 11 0 a5.5 5 0 0 1 11 0 a5.5 5 0 0 1 11 0 a5.5 5 0 0 1 11 0 a5.5 5 0 0 1 11 0 a5.5 5 0 0 1 11 0 a5.5 5 0 0 1 11 0 a5.5 5 0 0 1 11 0 a5.5 5 0 0 1 11 0 a5.5 5 0 0 1 11 0 a5.5 5 0 0 1 11 0 a5.5 5 0 0 1 11 0 a5.5 5 0 0 1 11 0 a5.5 5 0 0 1 11 0 a5.5 5 0 0 1 11 0 a5.5 5 0 0 1 11 0 a5.5 5 0 0 1 11 0 a5.5 5 0 0 1 11 0 a5.5 5 0 0 1 11 0 a5.5 5 0 0 1 11 0 a5.5 5 0 0 1 11 0 a5.5 5 0 0 1 11 0 a5.5 5 0 0 1 11 0 a5.5 5 0 0 1 11 0 a5.5 5 0 0 1 11 0 a5.5 5 0 0 1 11 0 a5.5 5 0 0 1 11 0 a5.5 5 0 0 1 11 0 a5.5 5 0 0 1 11 0 a5.5 5 0 0 1 11 0 a5.5 5 0 0 1 11 0 a5.5 5 0 0 1 11 0 a5.5 5 0 0 1 11 0 a5.5 5 0 0 1 11 0 a5.5 5 0 0 1 11 0 a5.5 5 0 0 1 11 0 a5.5 5 0 0 1 11 0 a5.5 5 0 0 1 11 0 L549 309 L0 309 Z"/>
    </svg>
    <div class="brand-seal" style="left:209px;top:77px;width:118px;height:118px"><span>VERELL</span></div>
    <h1 class="title" style="top:209px;font-size:45px;left:15px">PERFUMES</h1>
    <div class="rule left" style="left:72px;top:283px;width:78px"></div>
    <div class="tagline" style="left:150px;top:272px;width:237px;height:23px;font-size:16px;letter-spacing:2px">www.verellperfumes.com</div>
    <div class="rule right" style="left:387px;top:283px;width:80px"></div>
  </section>

  <p class="page-label" style="right:50px;top:52px">Inner Page 1</p>
  <section class="page" style="left:602px;top:74px">
    <div class="visual" role="img" aria-label="Mosaic of perfume bottle caps and letter shapes in rose, cream, terracotta and deep burgundy tones" style="background:linear-gradient(180deg,#8e3a30 0%,#ead8b4 28%,#e88a6a 50%,#7a2a24 75%,#b08a72 100%)"></div>
  </section>

  <p class="page-label" style="left:40px;top:404px">Inner Page 2</p>
  <section class="page" style="left:30px;top:426px">
    <svg class="band" width="549" height="309" viewBox="0 0 549 309" aria-hidden="true">
      <path fill="var(--brown)" d="M0 0 L549 0 L549 212 a5.5 5 0 0 1 -11 0 a5.5 5 0 0 1 -11 0 a5.5 5 0 0 1 -11 0 a5.5 5 0 0 1 -11 0 a5.5 5 0 0 1 -11 0 a5.5 5 0 0 1 -11 0 a5.5 5 0 0 1 -11 0 a5.5 5 0 0 1 -11 0 a5.5 5 0 0 1 -11 0 a5.5 5 0 0 1 -11 0 a5.5 5 0 0 1 -11 0 a5.5 5 0 0 1 -11 0 a5.5 5 0 0 1 -11 0 a5.5 5 0 0 1 -11 0 a5.5 5 0 0 1 -11 0 a5.5 5 0 0 1 -11 0 a5.5 5 0 0 1 -11 0 a5.5 5 0 0 1 -11 0 a5.5 5 0 0 1 -11 0 a5.5 5 0 0 1 -11 0 a5.5 5 0 0 1 -11 0 a5.5 5 0 0 1 -11 0 a5.5 5 0 0 1 -11 0 a5.5 5 0 0 1 -11 0 a5.5 5 0 0 1 -11 0 a5.5 5 0 0 1 -11 0 a5.5 5 0 0 1 -11 0 a5.5 5 0 0 1 -11 0 a5.5 5 0 0 1 -11 0 a5.5 5 0 0 1 -11 0 a5.5 5 0 0 1 -11 0 a5.5 5 0 0 1 -11 0 a5.5 5 0 0 1 -11 0 a5.5 5 0 0 1 -11 0 a5.5 5 0 0 1 -11 0 a5.5 5 0 0 1 -11 0 a5.5 5 0 0 1 -11 0 a5.5 5 0 0 1 -11 0 a5.5 5 0 0 1 -11 0 a5.5 5 0 0 1 -11 0 a5.5 5 0 0 1 -11 0 a5.5 5 0 0 1 -11 0 a5.5 5 0 0 1 -11 0 a5.5 5 0 0 1 -11 0 a5.5 5 0 0 1 -11 0 a5.5 5 0 0 1 -11 0 a5.5 5 0 0 1 -11 0 a5.5 5 0 0 1 -11 0 a5.5 5 0 0 1 -11 0 a5.5 5 0 0 1 -11 0 Z"/>
    </svg>
    <h2 class="title" style="top:36px;font-size:39px">VERELL PERFUMES LTD</h2>
    <div class="rule left" style="left:58px;top:104px;width:85px"></div>
    <div class="tagline" style="left:143px;top:92px;width:255px;height:24px;font-size:17px">Finest Materials Handcrafted</div>
    <div class="rule right" style="left:398px;top:104px;width:87px"></div>
    <div class="brand-seal" style="left:216px;top:145px;width:114px;height:114px"><span>VERELL</span></div>
    <p class="footer" style="left:24px">www.verellperfumes.com</p>
    <p class="footer" style="right:25px">Perfumer@verellperfumes.com I 1-604-555-0173</p>
  </section>

  <p class="page-label" style="right:52px;top:404px">Inner Page 3</p>
  <section class="page" style="left:602px;top:426px">
    <svg class="band" width="549" height="309" viewBox="0 0 549 309" aria-hidden="true">
      <path fill="var(--brown)" d="M0 0 L549 0 L549 95 a5.5 5 0 0 1 -11 0 a5.5 5 0 0 1 -11 0 a5.5 5 0 0 1 -11 0 a5.5 5 0 0 1 -11 0 a5.5 5 0 0 1 -11 0 a5.5 5 0 0 1 -11 0 a5.5 5 0 0 1 -11 0 a5.5 5 0 0 1 -11 0 a5.5 5 0 0 1 -11 0 a5.5 5 0 0 1 -11 0 a5.5 5 0 0 1 -11 0 a5.5 5 0 0 1 -11 0 a5.5 5 0 0 1 -11 0 a5.5 5 0 0 1 -11 0 a5.5 5 0 0 1 -11 0 a5.5 5 0 0 1 -11 0 a5.5 5 0 0 1 -11 0 a5.5 5 0 0 1 -11 0 a5.5 5 0 0 1 -11 0 a5.5 5 0 0 1 -11 0 a5.5 5 0 0 1 -11 0 a5.5 5 0 0 1 -11 0 a5.5 5 0 0 1 -11 0 a5.5 5 0 0 1 -11 0 a5.5 5 0 0 1 -11 0 a5.5 5 0 0 1 -11 0 a5.5 5 0 0 1 -11 0 a5.5 5 0 0 1 -11 0 a5.5 5 0 0 1 -11 0 a5.5 5 0 0 1 -11 0 a5.5 5 0 0 1 -11 0 a5.5 5 0 0 1 -11 0 a5.5 5 0 0 1 -11 0 a5.5 5 0 0 1 -11 0 a5.5 5 0 0 1 -11 0 a5.5 5 0 0 1 -11 0 a5.5 5 0 0 1 -11 0 a5.5 5 0 0 1 -11 0 a5.5 5 0 0 1 -11 0 a5.5 5 0 0 1 -11 0 a5.5 5 0 0 1 -11 0 a5.5 5 0 0 1 -11 0 a5.5 5 0 0 1 -11 0 a5.5 5 0 0 1 -11 0 a5.5 5 0 0 1 -11 0 a5.5 5 0 0 1 -11 0 a5.5 5 0 0 1 -11 0 a5.5 5 0 0 1 -11 0 a5.5 5 0 0 1 -11 0 a5.5 5 0 0 1 -11 0 Z"/>
    </svg>
    <h2 class="title" style="top:36px;font-size:39px">ABOUT ME</h2>
    <div class="portrait-frame"><div class="portrait" role="img" aria-label="Portrait photo of the perfumer in an embroidered jacket on a city street"></div></div>
    <h3 class="bio-name">DANIEL ARTHUR HALE</h3>
    <p class="bio-role">Self Educated Perfumer &nbsp; I &nbsp; Advocate for mental health</p>
    <ul class="timeline">
      <li><b>Born 1979</b>: Managed family Orchard to age 25</li>
      <li><b>Education</b>: Graphic Design &amp; Culinary arts</li>
      <li><b>2005 - 2015</b>: Tokyo, Kyoto student to Japanese artisians</li>
      <li><b>2015</b>: Return to Canada</li>
      <li><b>2015 - 2019</b>: Self-Study Perfumery</li>
      <li><b>December 2019</b>: Release “Amber Moss Chypre”</li>
    </ul>
    <p class="footer" style="left:24px">www.verellperfumes.com</p>
    <p class="footer" style="right:25px">Perfumer@verellperfumes.com I 1-604-555-0173</p>
  </section>

</main>
</body>
</html>
```